Cover Design for Product Catalog

I would like a cover design made for the front and back cover of our Ravenmoor Catalog.

Currently we were going to have a glass go from the front to back cover but we have decided it is not a good fit. Previously we used a big logo on the front cover and on the back cover it was there too(See old catalog file).

I have attached what our current design was going to look like including some of the interior pages to maybe give you ideas and make it flow.

Important things:
1. We want the background to be black and consistent with previous catalogs.
2. We want the tag line "Comfort - Protection - Performance" somewhere or the tagline "Independent, Growing and Innovating"
3. The logo should be big and easier to read such as it was in the old catalogs.
4. We like the chrome look and were planning to have it done as a special coating when printed. (I have attached a sales sheet file for reference)
5. We like how we have our trademarks on the back cover.

Attached is a competitor catalog cover we thought looks nice. We need our cover to stay with an industrial type of theme as we sell to the industrial safety market.

Target Market(s)

Industrial Safety Market. Personal Protective Equipment.

Industry/Entity Type

Safety

Requirements
Must have
• 1. We want the background to be black and consistent with previous catalogs.
• 2. We want the tag line "Comfort - Protection - Performance" somewhere or the tagline "Independent, Growing and Innovating"
• 3. The logo should be big and easier to read such as it was in the old catalogs.
• 4. We like the chrome look and were planning to have it done as a special coating when printed. (I have attached a sales sheet file for reference)
• 5. We like how we have our trademarks on the back cover.
• 6. Industrial safety market feel
Nice to have
• Cool effect, maybe to raise something on the page(when printed) like the competitor one had.
Should not have
• Action photos as we do not have many good action photos of people wearing our glasses.

```html
<!DOCTYPE html>
<html lang="en">
<head>
<meta charset="utf-8">
<title>Ravenmoor Catalog Covers</title>
<link rel="stylesheet" href="https://fonts.googleapis.com/css2?family=Quicksand:wght@400;500;700&display=swap">
<style>
  :root {
    --backdrop: #0c4b63;
    --cover-black: #04040a;
    --cover-navy: #0a0c24;
    --glow-blue: #3a3fe8;
    --chrome-light: #f2f4f6;
    --chrome-mid: #a9afb6;
    --chrome-dark: #5d636a;
    --ink-light: #e6e9ec;
  }
  * { box-sizing: border-box; margin: 0; padding: 0; }
  html, body {
    width: 1200px; height: 1200px; overflow: hidden;
    background: var(--backdrop);
    font-family: "Quicksand", sans-serif;
  }
  .spread { position: relative; width: 1200px; height: 1200px; }
  .cover {
    position: absolute; top: 220px; width: 540px; height: 760px;
    background: radial-gradient(ellipse at 50% 35%, var(--cover-navy) 0%, var(--cover-black) 70%);
    box-shadow: 0 14px 30px rgba(0,0,0,.45);
    overflow: hidden;
  }
  .cover--front { left: 40px; }
  .cover--back {
    left: 620px;
    background: radial-gradient(ellipse 60% 45% at 50% 28%, #2226b0 0%, #11136a 40%, var(--cover-black) 100%);
  }

  .brand { position: absolute; left: 56px; top: 64px; display: flex; align-items: center; gap: 18px; }
  .brand__mark { width: 58px; height: 58px; border-radius: 50%; background: var(--ink-light); flex: none; }
  .brand__name { font-weight: 700; font-size: 66px; color: var(--ink-light); line-height: 1; }
  .brand__sub {
    position: absolute; left: 134px; top: 142px;
    font-weight: 700; font-size: 20px; color: var(--ink-light); letter-spacing: 1px;
  }

  .product-shot { position: absolute; border-radius: 28px; }
  .cover--front .product-shot {
    left: 30px; top: 200px; width: 480px; height: 220px;
    background: linear-gradient(100deg, #7fa9e0 0%, #24324f 16%, #0f1220 26%, #1d7fe6 40%, #33a6f5 52%, #0e1426 66%, #6e7580 82%, #2b2f36 100%);
  }
  .cover--back .product-shot {
    left: 24px; top: 250px; width: 492px; height: 200px;
    background: linear-gradient(100deg, #9aa3ad 0%, #2c4fa0 14%, #3d6fc8 30%, #c9dbef 46%, #8fb2dc 56%, #13a37a 72%, #2fd08f 84%, #9aa3ad 100%);
  }
  .floor-glow {
    position: absolute; left: 80px; width: 380px; height: 36px;
    background: radial-gradient(ellipse at 50% 50%, rgba(90,100,255,.85) 0%, rgba(58,63,232,.4) 40%, transparent 75%);
  }
  .cover--front .floor-glow { top: 418px; }
  .cover--back .floor-glow { top: 448px; }

  .chrome-band { position: absolute; left: 0; width: 100%;
    background: linear-gradient(180deg, var(--chrome-dark) 0%, var(--chrome-light) 45%, var(--chrome-mid) 70%, var(--chrome-dark) 100%); }
  .chrome-band--thick { height: 14px; }
  .chrome-band--thin { height: 7px; }

  .tagline {
    position: absolute; left: 0; width: 100%; top: 640px; text-align: center;
    font-weight: 500; font-size: 27px; color: var(--ink-light); letter-spacing: .5px;
  }
  .tagline__rule { display: inline-block; width: 2px; height: 34px; background: var(--ink-light); vertical-align: middle; margin: 0 8px; }

  .contact {
    position: absolute; left: 40px; top: 626px; font-style: normal;
    font-weight: 700; font-size: 12px; line-height: 16px; color: var(--ink-light);
  }
  .back-brand { position: absolute; right: 30px; top: 650px; display: flex; align-items: center; gap: 6px; }
  .back-brand .brand__mark { width: 14px; height: 14px; }
  .back-brand .brand__name { font-size: 16px; }
</style>
</head>
<body>
<main class="spread">

  <section class="cover cover--front">
    <div class="brand">
      <span class="brand__mark"></span>
      <span class="brand__name">Ravenmoor</span>
    </div>
    <div class="brand__sub">Safety Eyewear</div>

    <div class="product-shot" role="img" aria-label="Product photo: blue mirrored wraparound safety glasses flanked by clear and smoke-lens pairs"></div>
    <div class="floor-glow"></div>

    <div class="chrome-band chrome-band--thick" style="top:572px"></div>
    <div class="chrome-band chrome-band--thin" style="top:598px"></div>
    <p class="tagline">Comfort<span class="tagline__rule"></span>Protection<span class="tagline__rule"></span>Performance</p>
    <div class="chrome-band chrome-band--thin" style="top:700px"></div>
    <div class="chrome-band chrome-band--thick" style="top:716px"></div>
  </section>

  <section class="cover cover--back">
    <div class="product-shot" role="img" aria-label="Product photo: blue mirrored glasses, clear safety goggle and green mirrored glasses"></div>
    <div class="floor-glow"></div>

    <div class="chrome-band chrome-band--thick" style="top:572px"></div>
    <div class="chrome-band chrome-band--thin" style="top:598px"></div>
    <address class="contact">
      2140 Foundry Ave NW<br>
      Halbrook, MN 55990<br>
      Phone: 555-014-2270<br>
      Email: sales@RavenmoorSafety.com<br>
      www.ravenmoorsafety.com
    </address>
    <div class="back-brand">
      <span class="brand__mark"></span>
      <span class="brand__name">Ravenmoor</span>
    </div>
    <div class="chrome-band chrome-band--thin" style="top:714px"></div>
    <div class="chrome-band chrome-band--thick" style="top:730px"></div>
  </section>

</main>
</body>
</html>
```